Redesign of Plastic Surgeon Website to fully responsive / modern feel

Hi

Our current website is out of date www.harbourlinecosmetic.org

We want a fresh / modern looking design
Needs to be fully responsive design that works extremely well on ipad and mobile device

Would like design for both full screen website and mobile

Have listed a few websites of other plastic surgeons we like
http://www.reformclinicdaily.com/
http://www.peterholtbymd.com/
http://www.corvanbeauty.com/
http://www.tidewellcontouring.com/

Menu needs to include
1. About Us
2. Procedures (see current website for example)
3. News
4. Patient Resources
5. Contact Us

We are flexible with colours / images / layout

I have uploaded a document that has some content - the face pages content is completed only

some of the procedures can have content upwards of 4000 words - total website can be large with over 40,000 words
Updates

Target Market(s)

Mainly women 20-60 85% of practice
Some men 15%

Industry/Entity Type

Plastic Surgery

Number of Pages Required

5+ page

Requirements
Must have
• We need designs for
• Homepage
• Internal pages
• 1. Landing pages for breast / body / face / non surgical main pages
• 2. Procedure pages for individual pages under each section - eg breast augmentation
• 3. About us pages - like meet the doctor, our staff, clinics
• 4. Contact page
• 5. Blog / News page
Nice to have
• See our list of websites for examples of designs we like
• Like full screen design with nice hero image
• Needs to have good to call to action messages on home page like
• Specials, procedure of the month, etc

```html
<!DOCTYPE html>
<html lang="en">
<head>
<meta charset="utf-8">
<title>Patient Resources – Harbourline Institute of Cosmetic Surgery</title>
<link href="https://fonts.googleapis.com/css2?family=Roboto:wght@400;500;700&family=Lora:wght@400&family=Oswald:wght@400&display=swap" rel="stylesheet">
<style>
:root{
  --pink:#c439b4;
  --pink-light:#d65ac8;
  --ink:#1b1b1b;
  --text:#6b6b6b;
  --hero:#4a4a4a;
  --footer:#454545;
  --footer-base:#3b3b3b;
  --footer-text:#cfcfcf;
  --green:#6cc04a;
  --white:#fff;
}
*{box-sizing:border-box;margin:0;padding:0}
html,body{width:881px;height:1200px;overflow:hidden;background:var(--white)}
body{position:relative;font-family:"Roboto",Arial,sans-serif;color:var(--text)}
.abs{position:absolute}

.topbar{left:0;top:0;width:881px;height:31px;background:#f7f7f7;border-bottom:1px solid #e6e6e6}
.topbar-info{left:181px;top:10px;font:400 9px "Lora",serif;color:#222;letter-spacing:.3px}
.topbar-social{right:20px;top:9px;display:flex;gap:12px;align-items:center}
.dot{width:8px;height:8px;border-radius:50%;background:#333}
.nav{left:0;top:31px;width:881px;height:45px;background:var(--white);border-bottom:1px solid #e3e3e3}
.nav-item{top:12px;font:400 9.5px "Lora",serif;color:#111;text-transform:uppercase;text-align:center;line-height:12px}

.brand{left:26px;top:40px;display:flex;align-items:center;gap:7px}
.brand-mark{width:11px;height:11px;background:var(--pink);flex:none}
.brand-name{font:500 10px/12.5px "Roboto",sans-serif;color:var(--ink)}

.hero{left:0;top:76px;width:881px;height:205px;background:radial-gradient(ellipse at 50% 40%,#8a8a8a 0%,#5a5a5a 35%,var(--hero) 70%)}
.hero-title{left:0;top:140px;width:881px;text-align:center;font:500 37px "Roboto",sans-serif;color:var(--white);letter-spacing:.5px}
.crumbs{left:0;top:182px;width:881px;text-align:center;font:400 10px "Oswald",sans-serif;color:var(--white);text-transform:uppercase}

.tab{left:315px;top:312px;width:251px;height:25px;background:#0d0d0d;color:var(--white);font:500 9.5px "Roboto",sans-serif;letter-spacing:1.2px;text-align:center;line-height:25px;text-transform:uppercase}
.tab em{font-style:normal;color:var(--pink-light)}

.section-title{top:395px;font:400 17px "Roboto",sans-serif;color:var(--ink)}
.portrait{left:43px;top:445px;width:251px;height:294px;background:linear-gradient(135deg,#d8d8d8,#9a9a9a 60%,#cfcfcf)}
.intro{left:312px;top:452px;width:250px}
.intro h2{font:400 11.5px/15.5px "Roboto",sans-serif;color:var(--ink);text-transform:uppercase;margin-bottom:6px}
.intro p{font:400 10px/15.7px "Roboto",sans-serif;color:var(--text);margin-bottom:15px}

.services{left:646px;top:452px;width:190px;list-style:none}
.services li{position:absolute;left:0;width:190px;font:400 8.5px/11px "Roboto",sans-serif;color:#444;padding-left:18px}
.services li svg{position:absolute;left:0;top:0}

.info-strip{left:42px;top:815px;width:792px;height:82px;display:flex;z-index:2}
.info{position:relative;height:82px;background:var(--pink);color:var(--white)}
.info.alt{background:var(--pink-light)}
.info h3{position:absolute;top:22px;font:700 9.5px "Roboto",sans-serif;text-transform:uppercase}
.info p{position:absolute;top:40px;font:400 8.5px/13px "Roboto",sans-serif}
.info svg{position:absolute;top:32px}

.footer{left:0;top:856px;width:881px;height:285px;background:var(--footer)}
.footer-brand{left:112px;top:975px;display:flex;align-items:center;gap:8px}
.footer-brand .brand-mark{background:#bdbdbd;width:12px;height:12px}
.footer-brand .brand-name{font:500 11px/14px "Roboto",sans-serif;color:#bdbdbd}
.footer-h{top:931px;font:500 12.5px "Roboto",sans-serif;color:var(--white);text-transform:uppercase}
.footer-h::after{content:"";position:absolute;left:0;top:22px;width:42px;height:2px;background:var(--pink)}
.svc-list{list-style:none;font:400 8.5px "Roboto",sans-serif;color:var(--footer-text)}
.svc-list li{height:21.7px}
.svc-list li::before{content:"›";margin-right:5px}
.news-text{left:611px;top:980px;width:225px;font:400 8.5px/11px "Roboto",sans-serif;color:var(--footer-text)}
.email{left:611px;top:1018px;width:157px;height:24px;background:#3e3e3e;border:1px solid #5c5c5c;font:400 8.5px/22px "Roboto",sans-serif;color:var(--white);padding-left:10px}
.send{left:768px;top:1017px;width:67px;height:25px;background:var(--pink);color:var(--white);font:500 8.5px/25px "Roboto",sans-serif;text-align:center;text-transform:uppercase}
.stay{left:612px;top:1062px;font:500 8.5px "Roboto",sans-serif;color:var(--white);text-transform:uppercase}
.foot-social{left:614px;top:1093px;display:flex;gap:24px}
.foot-social .dot{background:#9a9a9a}

.base{left:0;top:1141px;width:881px;height:59px;background:var(--footer-base)}
.copy{left:0;top:1156px;width:881px;text-align:center;font:400 8px "Roboto",sans-serif;color:#9a9a9a}
.base-links{left:0;top:1173px;width:881px;text-align:center;font:400 8.5px "Roboto",sans-serif;color:#9a9a9a;letter-spacing:2.6px}
</style>
</head>
<body>

<header>
  <div class="abs topbar">
    <div class="abs topbar-info">INFO &amp; RESERVATIONS:&nbsp; 02 5550 1234</div>
    <div class="abs topbar-social" aria-label="Social links">
      <span class="dot"></span><span class="dot"></span><span class="dot"></span><span class="dot"></span>
      <svg width="10" height="10" viewBox="0 0 10 10"><circle cx="4" cy="4" r="3" fill="none" stroke="#222" stroke-width="1.4"/><line x1="6.2" y1="6.2" x2="9" y2="9" stroke="#222" stroke-width="1.5"/></svg>
    </div>
  </div>
  <nav class="abs nav">
    <div class="abs nav-item" style="left:178px;top:13px">Our Practice</div>
    <div class="abs nav-item" style="left:263px">Surgical<br>Proc Edures</div>
    <div class="abs nav-item" style="left:346px;top:13px">News &amp; Views</div>
    <div class="abs nav-item" style="left:440px;top:13px">Before After Photos</div>
    <div class="abs nav-item" style="left:552px">Plastic<br>Surgery Reviews</div>
    <div class="abs nav-item" style="left:658px">Patient<br>Preparation</div>
    <div class="abs nav-item" style="left:754px;top:13px">FAQ</div>
    <div class="abs nav-item" style="left:797px;top:13px">Contact</div>
  </nav>
  <div class="abs brand">
    <span class="brand-mark"></span>
    <span class="brand-name">Harbourline Institute<br>of Cosmetic Surgery</span>
  </div>
</header>

<section>
  <div class="abs hero" role="img" aria-label="Black and white close-up portrait background"></div>
  <h1 class="abs hero-title">PATIENT RESOURCES</h1>
  <div class="abs crumbs">Home &nbsp;&nbsp;»&nbsp;&nbsp; Patient Resources</div>
</section>

<div class="abs tab"><em>Your First</em> Consultation</div>

<main>
  <h2 class="abs section-title" style="left:46px">Your First Consultation</h2>
  <h2 class="abs section-title" style="left:630px">Services</h2>

  <div class="abs portrait" role="img" aria-label="Black and white portrait of a woman"></div>

  <div class="abs intro">
    <h2>Be who you are and say what you feel, because those who mind don't matter, and those who matter don't mind.</h2>
    <p>Hello, I'm a UI/UX Designer &amp; Front End Developer from Dhaka, Bangladesh. I hold a master degree of Web Design from the St. Aldric University.</p>
    <p>I currently work at Vantora, where I spend most of my time crafting and working on awesome projects. Lorem ipsum dolor sit amet consectetuer Integer eleifend Cura bitur id ut. Quisque Aenean ut pede id elit ligula est mollis sapien magna. Urna turpis quis sagittis at ac Sed augue habitant tortor elit. Dolor Quisque et elit aliquam vitae habitant.</p>
  </div>

  <ul class="abs services">
    <li style="top:0"><svg width="10" height="10"><rect width="10" height="10" rx="2" fill="var(--green)"/><path d="M5 2v6M2 5h6" stroke="#fff" stroke-width="1.6"/></svg>Before your consultation</li>
    <li style="top:34px"><svg width="10" height="10"><rect width="10" height="10" rx="2" fill="var(--green)"/><path d="M5 2v6M2 5h6" stroke="#fff" stroke-width="1.6"/></svg>During your consultation</li>
    <li style="top:67px"><svg width="10" height="10"><rect width="10" height="10" rx="2" fill="var(--green)"/><path d="M5 2v6M2 5h6" stroke="#fff" stroke-width="1.6"/></svg>Discovery of 'Master Molecule' Could Improve Stem Cell...</li>
    <li style="top:102px"><svg width="10" height="10"><rect width="10" height="10" rx="2" fill="var(--green)"/><path d="M5 2v6M2 5h6" stroke="#fff" stroke-width="1.6"/></svg>Low Vitamin D Levels Linked to Weight Gain in Older Women</li>
    <li style="top:136px"><svg width="10" height="10"><rect width="10" height="10" rx="2" fill="var(--green)"/><path d="M5 2v6M2 5h6" stroke="#fff" stroke-width="1.6"/></svg>Low Vitamin D Levels Linked to Weight Gain in Older Women</li>
    <li style="top:176px"><svg width="10" height="10"><rect width="10" height="10" rx="2" fill="var(--green)"/><path d="M5 2v6M2 5h6" stroke="#fff" stroke-width="1.6"/></svg>Low Vitamin D Levels Linked to Weight Gain in Older Women</li>
  </ul>
</main>

<div class="abs info-strip">
  <div class="info" style="width:251px">
    <svg style="left:30px" width="14" height="19" viewBox="0 0 14 19"><path d="M7 0C3 0 0 3 0 7c0 5 7 12 7 12s7-7 7-12C14 3 11 0 7 0z" fill="#fff"/><circle cx="7" cy="7" r="2.6" fill="var(--pink)"/></svg>
    <h3 style="left:61px">Hospital Address</h3>
    <p style="left:64px">E12, Garden Lane, Harbour Point<br>Melbourne - 007</p>
  </div>
  <div class="info alt" style="width:270px">
    <svg style="left:33px" width="17" height="17" viewBox="0 0 24 24"><path d="M6.6 10.8a15.1 15.1 0 006.6 6.6l2.2-2.2c.3-.3.7-.4 1-.2 1.1.4 2.3.6 3.6.6.6 0 1 .4 1 1V20c0 .6-.4 1-1 1A17 17 0 013 4c0-.6.4-1 1-1h3.5c.6 0 1 .4 1 1 0 1.3.2 2.5.6 3.6.1.3 0 .7-.2 1z" fill="#fff"/></svg>
    <h3 style="left:68px">Emergency ( 24x7 )</h3>
    <p style="left:71px">02 5550 1234<br>Call Us Now- 24/7 Customer Support</p>
  </div>
  <div class="info" style="width:271px">
    <svg style="left:34px" width="21" height="16" viewBox="0 0 21 16"><rect x="1" y="1" width="19" height="14" fill="none" stroke="#fff" stroke-width="1.6"/><path d="M1 1l9.5 8L20 1" fill="none" stroke="#fff" stroke-width="1.6"/></svg>
    <h3 style="left:70px">Hospital Address</h3>
    <p style="left:74px">info@coralwellhealth.com<br>support@coralwellhealth.com</p>
  </div>
</div>

<footer>
  <div class="abs footer"></div>
  <div class="abs footer-brand">
    <span class="brand-mark"></span>
    <span class="brand-name">Harbourline Institute<br>of Cosmetic Surgery</span>
  </div>

  <h3 class="abs footer-h" style="left:326px">Our Services</h3>
  <ul class="abs svc-list" style="left:327px;top:981px">
    <li>Births</li><li>Pulmonary</li><li>Cardiology</li><li>Neurology</li><li>Traumatology</li><li>Neurology</li>
  </ul>
  <ul class="abs svc-list" style="left:424px;top:981px">
    <li>Dental</li><li>Nuclear magnetic</li><li>Pregnancy</li><li>For disabled</li><li>X-ray</li><li>Prosthese</li>
  </ul>

  <h3 class="abs footer-h" style="left:611px">Newsletter</h3>
  <p class="abs news-text">Accusamus et iusto odio dignissimos ducimus blanditiis praesentium quas molestias except.</p>
  <div class="abs email">Email Address</div>
  <div class="abs send">Send</div>
  <div class="abs stay">Stay Connected</div>
  <div class="abs foot-social" aria-label="Social links"><span class="dot"></span><span class="dot"></span><span class="dot"></span><span class="dot"></span></div>

  <div class="abs base"></div>
  <p class="abs copy">© Harbourline Institute of Cosmetic Surgery Dr Elliot Marsden Cosmetic Surgery Sydney Australia</p>
  <p class="abs base-links">Home | Disclaimer | Privacy | Sitemap | Feedback | Tell a friend | Contact Us | Find us on Social</p>
</footer>

</body>
</html>
```